PREMIUM AGENCY High End Business Card - A+++ Designers Wanted

** DO NOT ATTEMPT TO CONTACT ME THROUGH SEARCHING ON ZINTREL OR EMAILING ME THROUGH MY WEBSITE **

I need a fresh, contemporary business card designed using the logo attached (BRONSALK)

I have attached the font for BRONSALK

It must have a premium look and feel. The business card size must be STANDARD size.

You can submit either/both VERTICAL or HORIZONTAL designs.

FRONT: It must have the following sample information on

Paul Ardley
Director Operations
Mobile +61 452 118 906
Email paulardley@bronsalk.com
www.bronsalk.com

The REAR of the business card must have the words

CREATE INSPIRE TOMORROW

as part of the design, in the same font (NEXA) attached.

The words do not need to be in capitals, or on the same line, please design this as you see it best working.

ADDITIONAL INFORMATION
======================

The BRONSALK logo must be on the front of the card

I want Ultraviolet printing on the final design, to enhance either the NAME of the person OR the BRONSALK logo OR the words on the back of the card.

Target Market(s)

Agency, Advertising Agency, Creative, Designers

Industry/Entity Type

Media

Contact Information for Business Card

Design Agency, Contemporary, Premium look and feel, High Quality

Font styles to use
Serif
Sans Serif
Other font styles liked:
• ATTACHED TO PROJECT

Requirements
Must have
• BLACK & WHITE as the primary design, and if you feel there can be a highlighted colour, then this can be used.
• The Logo ICON attached is blue, this colour must not be changed.
• I have attached the partner brand BRONSALK MEDIA incase you need to manipulate the original files.
• ** DO NOT ATTEMPT TO CONTACT ME THROUGH SEARCHING ON ZINTREL OR EMAILING ME THROUGH MY WEBSITE **
Nice to have
• Must be Premium. I have attached some sample designs, that I like that would be a good inspiration for where this can be taken.
• My favourite design is is the KESTRAVUE2-BUSINESSCARD-TEMPLATE
Should not have
• No funny or silly standard / off the shelf designs

```html
<!DOCTYPE html>
<html lang="en">
<head>
<meta charset="utf-8">
<title>Bronsalk Media – Business Card Front</title>
<link rel="stylesheet" href="https://fonts.googleapis.com/css2?family=Nunito:wght@700;900&display=swap">
<style>
  :root {
    --band-top: #333333;
    --band-bottom: #262626;
    --text-light: #ffffff;
    --accent-blue: #29a9e1;
    --rule-blue: #2a9fd8;
  }
  html, body {
    margin: 0;
    padding: 0;
    width: 1200px;
    height: 699px;
    overflow: hidden;
    background: var(--band-bottom);
  }
  .card {
    position: relative;
    width: 1200px;
    height: 699px;
    background: var(--band-bottom);
    font-family: "Nunito", sans-serif;
    color: var(--text-light);
  }
  .card__header {
    position: absolute;
    left: 0;
    top: 0;
    width: 1200px;
    height: 287px;
    background: var(--band-top);
  }
  .brand {
    position: absolute;
    left: 32px;
    top: 60px;
    width: 276px;
    text-align: center;
  }
  .brand__mark {
    display: block;
    width: 72px;
    height: 72px;
    margin: 0 auto 66px;
    border-radius: 50%;
    background: var(--accent-blue);
  }
  .brand__name {
    display: block;
    font-weight: 700;
    font-size: 25px;
    letter-spacing: 1.5px;
    line-height: 1;
    white-space: nowrap;
  }
  .identity {
    position: absolute;
    right: 67px;
    top: 66px;
    text-align: right;
    text-transform: uppercase;
  }
  .identity__name {
    margin: 0;
    font-weight: 900;
    font-size: 60px;
    line-height: 1;
    letter-spacing: 1.5px;
  }
  .identity__role {
    margin: 14px 0 0;
    font-weight: 900;
    font-size: 40px;
    line-height: 1;
    letter-spacing: 1px;
  }
  .identity__rule {
    position: absolute;
    left: 572px;
    top: 197px;
    width: 562px;
    height: 1px;
    background: var(--rule-blue);
  }
  .contact {
    position: absolute;
    right: 67px;
    top: 458px;
    margin: 0;
    text-align: right;
    font-weight: 700;
    font-style: normal;
  }
  .contact__line {
    display: block;
    font-size: 36px;
    line-height: 1;
    white-space: nowrap;
  }
  .contact__phone { font-size: 38px; margin-bottom: 19px; }
  .contact__email { margin-bottom: 16px; }
</style>
</head>
<body>
  <main class="card">
    <header class="card__header">
      <div class="brand">
        <span class="brand__mark"></span>
        <span class="brand__name">BRONSALK MEDIA</span>
      </div>
      <div class="identity">
        <h1 class="identity__name">Paul Ardley</h1>
        <p class="identity__role">Director Operations</p>
      </div>
    </header>
    <div class="identity__rule"></div>
    <address class="contact">
      <span class="contact__line contact__phone">+61 452 118 906</span>
      <span class="contact__line contact__email">Email me at paulardley@bronsalk.com</span>
      <span class="contact__line contact__web">www.bronsalk.com</span>
    </address>
  </main>
</body>
</html>
```